Paws Home

Need Yard signs
Dimensions 24" wide and 18" high

Copy: Rescue does not mean "Damaged". It means they have been let down by humans.
Please adopt at: 217 W Brannock Ave, Tampa, Fl 33682
Open: Tues-Sun 10am - 7pm

I have attached a sample of the original ad. I can't use this because the resolution is too low and the type has to be big enough so that it can be seen 12 feet away.
I have also attached some photos you can use. The res may not be hi enough, but perhaps you can find some stock photography even these pics are not hi res enough.

Target Market(s)

animal lovers

Font styles to use
Sans Serif

Colors

Designer to choose colors to be used in the design.

Requirements
Must have
• Must be easy to read.

```html
<!DOCTYPE html>
<html lang="en">
<head>
<meta charset="utf-8">
<title>Paws Home – Yard Sign</title>
<link rel="stylesheet" href="https://fonts.googleapis.com/css2?family=Anton&family=Roboto:wght@700&family=Roboto+Condensed:wght@700&display=swap">
<style>
  :root {
    --sign-yellow: #ffd500;
    --fold-yellow: #c9a800;
    --forest-dark: #0f2a17;
    --forest-mid: #1f4a28;
    --forest-light: #2f6a35;
    --coat-cream: #e9e1d2;
    --ink-black: #0a0a0a;
    --paper-white: #ffffff;
  }
  * { margin: 0; padding: 0; box-sizing: border-box; }
  html, body {
    width: 1200px;
    height: 900px;
    overflow: hidden;
    background: var(--forest-dark);
  }
  .yard-sign {
    position: relative;
    width: 1200px;
    height: 900px;
    overflow: hidden;
  }
  .backdrop-photo {
    position: absolute;
    inset: 0;
    background:
      radial-gradient(ellipse 330px 420px at 940px 620px, var(--coat-cream) 0%, rgba(233,225,210,0.85) 55%, rgba(233,225,210,0) 100%),
      radial-gradient(ellipse 700px 500px at 300px 250px, var(--forest-light) 0%, rgba(47,106,53,0) 70%),
      linear-gradient(160deg, var(--forest-mid) 0%, var(--forest-dark) 100%);
  }
  .headline-top {
    position: absolute;
    left: 60px;
    top: 48px;
    font-family: "Roboto", sans-serif;
    font-weight: 700;
    font-size: 82px;
    line-height: 1;
    color: var(--sign-yellow);
    letter-spacing: 0.5px;
    white-space: nowrap;
  }
  .headline-key {
    position: absolute;
    left: 40px;
    top: 156px;
    font-family: "Anton", sans-serif;
    font-size: 132px;
    line-height: 1;
    color: var(--sign-yellow);
    white-space: nowrap;
  }
  .headline-key .quote-mark {
    font-size: 110px;
    vertical-align: 18px;
  }
  .subline {
    position: absolute;
    left: 68px;
    top: 306px;
    font-family: "Roboto Condensed", sans-serif;
    font-weight: 700;
    font-size: 44px;
    line-height: 54px;
    color: var(--paper-white);
  }
  .adopt-banner {
    position: absolute;
    left: 26px;
    top: 538px;
    width: 472px;
    height: 148px;
  }
  .adopt-banner svg {
    position: absolute;
    inset: 0;
  }
  .adopt-banner .banner-label {
    position: absolute;
    left: 24px;
    top: 22px;
    font-family: "Anton", sans-serif;
    font-size: 60px;
    line-height: 1;
    color: var(--ink-black);
    white-space: nowrap;
  }
  .shelter-address {
    position: absolute;
    left: 46px;
    top: 664px;
    font-family: "Anton", sans-serif;
    font-size: 44px;
    line-height: 52px;
    color: var(--paper-white);
  }
  .opening-hours {
    position: absolute;
    left: 44px;
    top: 784px;
    font-family: "Roboto Condensed", sans-serif;
    font-weight: 700;
    font-size: 56px;
    line-height: 1;
    color: var(--sign-yellow);
    white-space: nowrap;
    letter-spacing: 0.5px;
  }
</style>
</head>
<body>
  <main class="yard-sign">
    <div class="backdrop-photo" role="img" aria-label="Photo of a white Labrador in profile wearing a red collar, against blurred green foliage"></div>

    <h1 class="headline-top">RESCUE DOES NOT MEAN</h1>
    <p class="headline-key"><span class="quote-mark">“</span>DAMAGED.<span class="quote-mark">”</span></p>

    <p class="subline">IT MEANS THEY HAVE<br>BEEN LET DOWN<br>BY HUMANS.</p>

    <div class="adopt-banner">
      <svg width="472" height="148" viewBox="0 0 472 148" aria-hidden="true">
        <polygon points="434,114 470,114 418,146" fill="var(--fold-yellow)"/>
        <polygon points="0,0 434,0 470,114 0,114" fill="var(--sign-yellow)"/>
      </svg>
      <span class="banner-label">PLEASE ADOPT AT</span>
    </div>

    <address class="shelter-address" style="font-style: normal;">217 W BRANNOCK AVE,<br>TAMPA, FL 33682</address>

    <p class="opening-hours">OPEN: TUES-SUN 10AM - 7PM</p>
  </main>
</body>
</html>
```